Credit card acceptance poster

I need a poster explaining to my customers that the washers and dryers at my laundromat accept credit card payments and most mobile wallet payments. I have attached a flyer I made. It looks terrible so I need help. The cc readers accept: ZELO, TRUVENBANK, ORBINTAL, COLDRIDGE FUNDCO, MERVALE TAP, TREVO WAVE, AND ODELIX SWIPE.

Colors
0054AA
0677BA
7BADD7
CADEEF
E8F1F8

```html
<!DOCTYPE html>
<html lang="en">
<head>
<meta charset="utf-8">
<title>Card Payments Accepted – Tidemark Laundromat</title>
<link rel="stylesheet" href="https://fonts.googleapis.com/css2?family=Anton&family=Bebas+Neue&family=Catamaran:wght@600;700&family=Montserrat:wght@800&display=swap">
<style>
  :root {
    --blue-deep: #0054AA;
    --blue-mid: #0677BA;
    --blue-soft: #7BADD7;
    --blue-pale: #CADEEF;
    --blue-mist: #E8F1F8;
    --navy-band: #2A5B92;
    --ink: #2B2B2B;
    --body-ink: #333333;
    --white: #FFFFFF;
    --card-line: #9A9A9A;
    --panel: #EEF0F2;
  }
  * { box-sizing: border-box; margin: 0; padding: 0; }
  html, body { width: 988px; height: 1200px; overflow: hidden; background: var(--white); }
  .poster {
    position: relative; width: 988px; height: 1200px; overflow: hidden;
    background: var(--white);
    font-family: "Catamaran", sans-serif;
  }
  .splash { position: absolute; }
  .splash--top { left: 0; top: 0; width: 988px; height: 330px; }
  .splash--mid { left: 0; top: 330px; width: 988px; height: 650px; }
  .splash--bottom { left: 0; top: 980px; width: 560px; height: 220px; }
  .frame {
    position: absolute; left: 28px; top: 34px; right: 30px; bottom: 34px;
    border: 2px solid var(--blue-mid);
  }
  .headline-band {
    position: absolute; left: 119px; top: 203px; width: 750px; height: 90px;
    background: var(--navy-band); color: var(--white);
    font-family: "Montserrat", sans-serif; font-weight: 800; font-size: 50px;
    display: flex; align-items: center; justify-content: center; letter-spacing: 0.5px;
  }
  .headline-main {
    position: absolute; left: 0; width: 988px; top: 312px; text-align: center;
    font-family: "Anton", sans-serif; font-size: 124px; line-height: 1.0;
    color: var(--ink); letter-spacing: 1px;
    transform: scaleX(1.14); transform-origin: 50% 0;
  }
  .accept-pill {
    position: absolute; left: 68px; top: 511px; width: 851px; height: 106px;
    border-radius: 53px;
    background: linear-gradient(180deg, var(--blue-mid), var(--blue-deep));
    color: var(--white); font-family: "Bebas Neue", sans-serif; font-size: 94px;
    display: flex; align-items: center; justify-content: center; padding-top: 6px;
  }
  .accept-copy {
    position: absolute; left: 0; width: 988px; top: 632px; text-align: center;
    font-weight: 600; font-size: 41px; line-height: 56px; color: var(--body-ink);
  }
  .method-panel {
    position: absolute; top: 778px; height: 93px; background: var(--panel);
    border-radius: 6px; display: flex; align-items: center; justify-content: space-evenly;
    box-shadow: 0 8px 10px -6px rgba(0,0,0,0.2);
  }
  .method-panel--cards { left: 69px; width: 476px; }
  .method-panel--wallets { left: 555px; width: 364px; }
  .method-tile {
    width: 97px; height: 60px; background: var(--white);
    border: 1.5px solid var(--card-line); border-radius: 5px;
    display: flex; align-items: center; justify-content: center; text-align: center;
    font-weight: 700; font-size: 14px; line-height: 15px; color: var(--blue-deep);
    padding: 0 4px;
  }
  .brand {
    position: absolute; left: 490px; top: 990px;
    display: flex; align-items: center; gap: 18px;
  }
  .brand-dot { width: 74px; height: 74px; border-radius: 50%; background: var(--blue-mid); }
  .brand-name {
    font-weight: 700; font-size: 46px; line-height: 46px; color: var(--blue-deep);
  }
</style>
</head>
<body>
  <main class="poster">
    <div class="splash splash--top" role="img" aria-label="Blue water splash sweeping across the top of the poster"
         style="background: linear-gradient(180deg, var(--blue-mid) 0%, var(--blue-soft) 45%, var(--blue-pale) 75%, rgba(255,255,255,0) 100%);"></div>
    <div class="splash splash--mid" role="img" aria-label="Faint pale blue water ripples behind the text"
         style="background: radial-gradient(ellipse at 50% 45%, var(--blue-mist) 0%, rgba(232,241,248,0.6) 55%, rgba(255,255,255,0) 80%);"></div>
    <div class="splash splash--bottom" role="img" aria-label="Blue water splash in the lower left corner"
         style="background: radial-gradient(ellipse at 0% 100%, var(--blue-mid) 0%, var(--blue-soft) 40%, var(--blue-pale) 60%, rgba(255,255,255,0) 80%);"></div>

    <div class="frame"></div>

    <h2 class="headline-band">NO BILLS OR COINS?</h2>
    <h1 class="headline-main">NO PROBLEM!</h1>

    <div class="accept-pill">OUR MECHINES ACCEPT</div>
    <p class="accept-copy">Credit Card Payments and<br>Most Mobile Wallet applications.</p>

    <div class="method-panel method-panel--cards">
      <span class="method-tile">ZELO</span>
      <span class="method-tile">TRUVENBANK</span>
      <span class="method-tile">ORBINTAL</span>
      <span class="method-tile">COLDRIDGE FUNDCO</span>
    </div>
    <div class="method-panel method-panel--wallets">
      <span class="method-tile">MERVALE TAP</span>
      <span class="method-tile">TREVO WAVE</span>
      <span class="method-tile">ODELIX SWIPE</span>
    </div>

    <div class="brand">
      <span class="brand-dot"></span>
      <span class="brand-name">TIDEMARK<br>LAUNDROMAT</span>
    </div>
  </main>
</body>
</html>
```